Commercial Security Landing Page

We're looking for a simple customizable Bootstrap based single landing page similar to http://gridtemplex.net/preview/GT482K913

I have attached our Full Logo to incorporate into the design.
I can also attach other assets if required.

We're in the Commercial Security Industry, we specialize in (These must be included on the site):
- CCTV
- Access Control
- Automation
- Fire Monitoring
- Theft Protection/Burglar Alarms

More information:
We install these systems in customers businesses to protect them from theft, fire, etc. We do very high quality installs and only use the highest quality equipment for each customer. We do not do network security or anything like that, we focus completely in protecting businesses and homes through the use of CCTV, Access Control, Automation such as (light control, garage control, flood protection, etc), we also handle fire monitoring, theft protection, and burglar alarms.

Specs/Requirements:
- Must not be built with WordPress.
- Must be built using Twitter Bootstrap
- Any images used must not be copyright protected or contain royalties.
- Eye Catching Stock Photos or Placeholder so that we can replace with our own photos.
- SEO Friendly
- Easily adjustable
- Contains a contact form
- Customized to our industry.
- Must be "modern" and scalable across all devices.

Colors we like:
- #0C9ED9
- #595A5C
- #414142

Target Market(s)

Business Owners, Home Owners, Enterprise

Industry/Entity Type

Security Service

Coding

Coded - Design and coding required

Font styles to use
Sans Serif

Requirements
Must have
• Must contain highlights of the following bullet points:
• - CCTV
• - Access Control
• - Automation
• - Fire Monitoring
• - Theft Protection/Burglar Alarms
Nice to have
• - Twitter Bootstrap
• - Any images used must not be copyright protected or contain royalties.
• - Eye Catching Stock Photos or Placeholder so that we can replace with our own photos.
• - SEO Friendly
• Partner Section (Showing off our partners):
• Vexlo.net (https://www.vexlo.net/)
• Tarnel Gate (http://www.tarnelgate.net/)
• BQM (http://www.brenwickquillmoor.net/)
Should not have
• Should not be built on Wordpress

```html
<!DOCTYPE html>
<html lang="en">
<head>
<meta charset="utf-8">
<title>Corvane – Commercial Security</title>
<link rel="stylesheet" href="https://fonts.googleapis.com/css2?family=Poppins:ital,wght@0,300;0,400;0,500;0,600;1,400&display=swap">
<style>
:root{
  --blue:#0c9ed9;
  --blue-deep:#1a8fcc;
  --grey:#595a5c;
  --dark:#414142;
  --ink:#2a2a2b;
  --footer:#262627;
  --panel:#bdbec0;
  --light:#f3f3f3;
  --white:#fff;
}
*{box-sizing:border-box;margin:0;padding:0}
html,body{width:1200px;height:3622px;overflow:hidden}
body{position:relative;font-family:'Poppins',sans-serif;color:var(--grey);background:var(--white)}
.abs{position:absolute}
.brand{display:flex;align-items:center;gap:10px;font-weight:600;color:var(--blue);letter-spacing:.5px}
.brand .mark{display:block;background:var(--blue)}
/* header */
.site-header{left:0;top:0;width:1200px;height:68px;background:var(--white);box-shadow:0 1px 4px rgba(0,0,0,.12);z-index:3}
.site-header .brand{position:absolute;left:113px;top:14px;font-size:34px}
.site-header .brand .mark{width:30px;height:30px;border-radius:4px}
.nav a{position:absolute;top:22px;font-size:15px;color:var(--grey);text-decoration:none}
.nav a.active{color:var(--blue);border:1.5px solid var(--blue);border-radius:4px;padding:3px 18px;top:18px}
/* hero */
.hero{left:0;top:68px;width:1200px;height:601px;background:linear-gradient(100deg,#8c939a 0%,#6d747b 40%,#3a3e44 70%,#25282c 100%)}
.hero-card{left:121px;top:188px;width:422px;height:331px;border:3px solid var(--blue);border-radius:60px 60px 60px 60px;background:rgba(25,27,30,.82);box-shadow:0 0 0 6px rgba(12,158,217,.35);text-align:center;padding-top:70px}
.hero-card h1{font-weight:400;color:var(--white);font-size:54px;line-height:62px}
.hero-card p{color:var(--blue);font-size:29px;letter-spacing:1px;margin-top:18px}
/* welcome */
.welcome{left:0;top:669px;width:1200px;height:338px;background:linear-gradient(#fafafa,#f0f0f0)}
.section-title{position:absolute;left:0;width:1200px;text-align:center;font-weight:500;font-size:25px;color:var(--ink);text-transform:uppercase}
.rule{position:absolute;left:425px;width:350px;height:1px;background:#c7c7c7}
.rule::after{content:"";position:absolute;left:168px;top:-1px;border:7px solid transparent;border-top-color:var(--blue);border-bottom:0}
.welcome-title{top:58px;display:flex;justify-content:center;align-items:center;gap:10px}
.welcome-title .brand{font-size:32px;text-transform:none}
.welcome-title .brand .mark{width:26px;height:26px;border-radius:4px}
.body-copy{position:absolute;left:120px;width:960px;text-align:center;font-size:11.5px;line-height:22px;color:var(--grey)}
.btn{position:absolute;background:var(--blue);color:var(--white);font-size:12px;font-weight:600;text-transform:uppercase;text-align:center;border-radius:4px}
/* services */
.services{left:0;top:1007px;width:1200px;height:780px;background:var(--blue)}
.services .section-title,.services .body-copy{color:var(--white)}
.services .rule{background:rgba(255,255,255,.6)}
.services .rule::after{border-top-color:var(--white)}
.svc-label{position:absolute;color:var(--white);font-weight:600;font-size:17px;text-transform:uppercase}
.svc-frame{position:absolute;border:4px solid var(--white);border-radius:36px;padding:6px;box-shadow:0 0 0 3px var(--blue),0 0 0 6px var(--white)}
.svc-frame .photo{width:100%;height:100%;border-radius:26px}
.hub{left:483px;top:1526px;width:234px;height:188px;border:6px solid var(--white);border-radius:40px;display:flex;align-items:center;justify-content:center;gap:12px;color:var(--white);font-weight:600;font-size:30px}
.hub .mark{width:22px;height:22px;background:var(--white);border-radius:50%}
/* testimonials */
.avatar{position:absolute;width:72px;height:72px;border-radius:50%;background:#d9d9d9;border:3px solid #ececec}
.avatar.current{background:linear-gradient(135deg,#3f6f95,#c89a7e);border-color:#fff;box-shadow:0 0 0 1px #ddd}
.quote{left:176px;top:2052px;width:845px;height:114px;background:#f1f1f2;border:1px solid #e2e2e2;border-radius:4px;box-shadow:0 3px 4px rgba(0,0,0,.08);text-align:center;font-style:italic;font-size:12.5px;line-height:24px;padding:14px 50px;color:var(--grey)}
.quote::before,.quote::after{position:absolute;font-size:40px;color:#c8c8c8;font-style:normal}
.quote::before{content:"\201C";left:24px;top:4px}
.quote::after{content:"\201D";right:30px;bottom:-20px}
/* contact */
.contact{left:0;top:2221px;width:1200px;height:483px;background:var(--panel)}
.contact .section-title{color:var(--white)}
.contact .rule{background:rgba(255,255,255,.7)}
.field{position:absolute;background:var(--white);font-size:13px;color:var(--grey);padding:10px 14px}
/* blog */
.post{position:absolute;top:2837px;width:306px}
.post .date{position:absolute;left:0;top:0;width:42px;height:48px;background:var(--blue);color:var(--white);text-align:center;font-weight:600;font-size:17px;line-height:22px;padding-top:4px}
.post .date small{display:block;font-size:11px;font-weight:400;line-height:14px}
.post h3{position:absolute;left:54px;top:0;width:250px;font-size:14px;font-weight:500;line-height:21px;color:var(--ink)}
.post .thumb{position:absolute;left:0;top:63px;width:306px;height:147px}
.post p{position:absolute;left:0;top:226px;width:306px;font-size:11px;line-height:22px;color:var(--grey)}
/* footer */
.site-footer{left:0;top:3202px;width:1200px;height:420px;background:var(--footer)}
.partners{left:113px;top:3202px;width:974px;height:96px;background:var(--white);border-radius:0 0 50% 50% / 0 0 40px 40px;display:flex;justify-content:center;align-items:center;gap:80px}
.partner{display:flex;align-items:center;gap:10px;font-weight:600;font-size:24px;color:var(--dark)}
.partner .mark{width:30px;height:30px;background:var(--blue)}
.partner .mark.round{border-radius:50%;background:#f0a030}
.partner .mark.sq{background:#c24a2c}
.site-footer .brand{position:absolute;left:113px;top:3412px;font-size:50px}
.site-footer .brand .mark{width:40px;height:40px;border-radius:6px}
.foot-h{position:absolute;color:var(--white);font-weight:600;font-size:15px;text-transform:uppercase;letter-spacing:.5px}
.links{position:absolute;left:546px;top:3400px;list-style:none}
.links li{font-size:12px;color:#d0d0d0;line-height:30px}
.links li::before{content:"›";margin-right:8px;color:#d0d0d0}
.info{position:absolute;left:809px;font-size:12px;color:#d0d0d0;line-height:17px;display:flex;gap:12px}
.info b{color:var(--white);font-weight:600}
.copyright{left:0;top:3583px;width:1200px;text-align:center;font-size:11px;color:#cfcfcf}
.foot-rule{left:113px;top:3562px;width:974px;height:1px;background:#3a3a3b}
</style>
</head>
<body>

<header class="site-header abs">
  <div class="brand"><span class="mark"></span>Corvane</div>
  <nav class="nav">
    <a class="active" href="#" style="left:555px">Home</a>
    <a href="#" style="left:680px">About</a>
    <a href="#" style="left:788px">Services</a>
    <a href="#" style="left:914px">Blog</a>
    <a href="#" style="left:1016px">Contact</a>
  </nav>
</header>

<section class="hero abs" role="img" aria-label="Close-up photo of a security surveillance camera"></section>
<div class="hero-card abs">
  <h1>Professional<br>&amp; Powerful</h1>
  <p>SECURITY PROTECTION</p>
</div>

<section class="welcome abs">
  <h2 class="section-title welcome-title">Welcome to <span class="brand"><span class="mark"></span>Corvane</span></h2>
  <div class="rule" style="top:108px"></div>
  <p class="body-copy" style="top:128px">Welcome enim ad minim veniam, quis nostrud exercitation ullamco laboris nisi ut aliquip ex ea commodo consequat. Duis aute irure dolor in reprehenderit in voluptate velit esse cillum dolore eu fugiat nulla pariatur. Excepteur sint occaecat cupidatat non proident, sunt Duis aute irure dolor in reprehenderit in voluptate velit esse cillum dolore eu fugiat nulla pariatur in culpa qui officia deserunt mollitanim id . Duis aute irure dolor in reprehenderit in voluptate velit esse cillum dolore eu fugiat nulla pariatur in culpa qui officia deserunt mollitanim id est laborum.</p>
  <div class="btn" style="left:543px;top:246px;width:77px;height:28px;line-height:28px">More</div>
</section>

<section class="services abs">
  <h2 class="section-title" style="top:50px;color:#fff">Our Services</h2>
  <div class="rule" style="top:96px"></div>
  <p class="body-copy" style="top:118px">Welcome enim ad minim veniam, quis nostrud exercitation ullamco laboris nisi ut aliquip ex ea commodo consequat. Duis aute irure dolor in reprehenderit in voluptate velit esse cillum dolore eu fugiat nulla pariatur. Excepteur sint occaecat cupidatat non proident.</p>
</section>

<svg class="abs" style="left:0;top:1007px" width="1200" height="780" viewBox="0 1007 1200 780" aria-hidden="true">
  <defs><marker id="head" viewBox="0 0 10 10" refX="9" refY="5" markerWidth="8" markerHeight="8" orient="auto"><path d="M0 0L10 5L0 10" fill="none" stroke="#fff" stroke-width="1.6"/></marker></defs>
  <g stroke="#fff" stroke-width="2.5" fill="none" marker-end="url(#head)">
    <line x1="606" y1="1512" x2="606" y2="1418"/>
    <line x1="470" y1="1570" x2="384" y2="1484"/>
    <line x1="730" y1="1570" x2="820" y2="1484"/>
    <line x1="470" y1="1636" x2="332" y2="1636"/>
    <line x1="730" y1="1636" x2="868" y2="1636"/>
  </g>
</svg>

<div class="svc-label" style="left:186px;top:1263px">Access Control</div>
<div class="svc-frame" style="left:169px;top:1304px;width:212px;height:154px"><div class="photo" role="img" aria-label="Photo of a hand holding an access card to a reader" style="background:linear-gradient(135deg,#bfc4c8,#6b6f73)"></div></div>

<div class="svc-label" style="left:521px;top:1210px">Fire Monitoring</div>
<div class="svc-frame" style="left:500px;top:1241px;width:210px;height:157px"><div class="photo" role="img" aria-label="Photo of a red fire alarm on a wall" style="background:linear-gradient(135deg,#f2efec,#c9bfb8 60%,#b04038)"></div></div>

<div class="svc-label" style="left:864px;top:1263px">Automation</div>
<div class="svc-frame" style="left:823px;top:1304px;width:210px;height:154px"><div class="photo" role="img" aria-label="Photo of security staff at a building entrance" style="background:linear-gradient(135deg,#e0ddd8,#8a8f96 60%,#3e4450)"></div></div>

<div class="svc-label" style="left:196px;top:1516px">CCTV</div>
<div class="svc-frame" style="left:113px;top:1557px;width:203px;height:155px"><div class="photo" role="img" aria-label="Photo of a CCTV camera in an office" style="background:linear-gradient(135deg,#f0f0f0,#a8a8a8 55%,#c5412f)"></div></div>

<div class="svc-label" style="left:893px;top:1518px">Theft Protection</div>
<div class="svc-frame" style="left:881px;top:1557px;width:206px;height:155px"><div class="photo" role="img" aria-label="Photo of a padlock and chain securing a door" style="background:linear-gradient(135deg,#3a4250,#1e2228 60%,#b8903a)"></div></div>

<div class="hub abs"><span class="mark"></span>Corvane</div>

<section class="abs" style="left:0;top:1787px;width:1200px;height:434px">
  <h2 class="section-title" style="top:52px">Testimonials</h2>
  <div class="rule" style="top:98px"></div>
</section>
<div class="avatar" style="left:271px;top:1934px" role="img" aria-label="Client photo placeholder"></div>
<div class="avatar current" style="left:563px;top:1934px" role="img" aria-label="Featured client photo"></div>
<div class="avatar" style="left:855px;top:1934px" role="img" aria-label="Client photo placeholder"></div>
<blockquote class="quote abs">Lorem ipsum dolor sit amet, consectetuer adipiscing elit, sed diam nonummy nibh euismod tincidunt ut laoreet dolore magna aliquam erat volutpat. Ut wisi enim ad minim veniam, quis nostrud exerci tation ullamcorper suscipit lobortis nisl ut aliquip ex ea commodo consequat. Duis autem vel eum&nbsp; dignissim qui blandit praesent luptatum zzril delenit augue.</blockquote>

<section class="contact abs">
  <h2 class="section-title" style="top:56px">Contact Us</h2>
  <div class="rule" style="top:100px"></div>
</section>
<div class="field" style="left:249px;top:2364px;width:343px;height:41px">Name:</div>
<div class="field" style="left:606px;top:2364px;width:345px;height:41px">Email:</div>
<div class="field" style="left:249px;top:2419px;width:343px;height:44px">Phone No:</div>
<div class="field" style="left:606px;top:2419px;width:345px;height:44px">Subject:</div>
<div class="field" style="left:249px;top:2477px;width:702px;height:99px">Phone No:</div>
<div class="btn" style="left:548px;top:2610px;width:104px;height:31px;line-height:31px">Submit</div>

<section class="abs" style="left:0;top:2704px;width:1200px;height:498px">
  <h2 class="section-title" style="top:50px">From the Blog</h2>
  <div class="rule" style="top:96px"></div>
</section>
<article class="post" style="left:113px">
  <div class="date">10<small>Dec</small></div>
  <h3>Nonummy nibh euismod tincidunt ut laoreet dolore magna</h3>
  <div class="thumb" role="img" aria-label="Photo of a hand turning a key in a door lock" style="background:linear-gradient(135deg,#e8e8e8,#4a4a4a 50%,#d0b060)"></div>
  <p>Sed diam nonummy nibh euismod tincidunt ut laoreet dolore magna aliquam erat volutpat enim ad minim veniam quis nostrud exerci tatullamco suscipit lobortis nisl ut aliquip...</p>
</article>
<article class="post" style="left:444px">
  <div class="date">10<small>Dec</small></div>
  <h3>Nonummy nibh euismod tincidunt ut laoreet dolore magna</h3>
  <div class="thumb" role="img" aria-label="Photo of hands holding a glowing globe" style="background:linear-gradient(135deg,#2c1e3a,#6a3f6a 50%,#c89070)"></div>
  <p>Sed diam nonummy nibh euismod tincidunt ut laoreet dolore magna aliquam erat volutpat enim ad minim veniam quis nostrud exerci tatullamco suscipit lobortis nisl ut aliquip...</p>
</article>
<article class="post" style="left:777px">
  <div class="date">10<small>Dec</small></div>
  <h3>Nonummy nibh euismod tincidunt ut laoreet dolore magna</h3>
  <div class="thumb" role="img" aria-label="Photo of a fingerprint access panel beside a glass door" style="background:linear-gradient(135deg,#e6eef2,#9eb4c0 60%,#2c3640)"></div>
  <p>Sed diam nonummy nibh euismod tincidunt ut laoreet dolore magna aliquam erat volutpat enim ad minim veniam quis nostrud exerci tatullamco suscipit lobortis nisl ut aliquip...</p>
</article>

<footer class="site-footer abs"></footer>
<div class="partners abs">
  <div class="partner"><span class="mark round"></span>Tarnel Gate</div>
  <div class="partner"><span class="mark"></span>Vexlo.net</div>
  <div class="partner"><span class="mark sq"></span>BQM</div>
</div>
<div class="brand abs" style="left:113px;top:3412px;font-size:50px"><span class="mark" style="width:40px;height:40px;border-radius:6px"></span>Corvane</div>

<div class="foot-h" style="left:546px;top:3366px">Quick Links</div>
<ul class="links">
  <li>Home</li><li>About Corvane</li><li>Our Services</li><li>Our Blog</li><li>Contact Us</li>
</ul>

<div class="foot-h" style="left:809px;top:3366px">Contact Info</div>
<div class="info" style="top:3404px">
  <svg width="12" height="16" viewBox="0 0 12 16" aria-hidden="true"><path d="M6 0a6 6 0 0 0-6 6c0 4.5 6 10 6 10s6-5.5 6-10a6 6 0 0 0-6-6zm0 8.5A2.5 2.5 0 1 1 6 3.5a2.5 2.5 0 0 1 0 5z" fill="#fff"/></svg>
  <div><b>Main Office</b><br>Corvane Security&nbsp; Solutions dolor lorem Ipsum<br>ut wisi enim ad minim.</div>
</div>
<div class="info" style="top:3472px">
  <svg width="14" height="14" viewBox="0 0 24 24" aria-hidden="true"><path d="M6.6 10.8a15 15 0 0 0 6.6 6.6l2.2-2.2a1 1 0 0 1 1-.25 11.4 11.4 0 0 0 3.6.57 1 1 0 0 1 1 1V20a1 1 0 0 1-1 1A17 17 0 0 1 3 4a1 1 0 0 1 1-1h3.5a1 1 0 0 1 1 1c0 1.25.2 2.45.57 3.57a1 1 0 0 1-.25 1z" fill="#fff"/></svg>
  <b style="font-size:14px">123-456-7890</b>
</div>
<div class="info" style="top:3500px">
  <svg width="14" height="12" viewBox="0 0 14 12" aria-hidden="true"><rect x="0" y="1" width="14" height="10" fill="#fff"/><path d="M0 1l7 5 7-5" fill="none" stroke="#262627" stroke-width="1.3"/></svg>
  <span>info@corvane.net</span>
</div>

<div class="foot-rule abs"></div>
<p class="copyright abs">All rights Reserved 2017</p>

</body>
</html>
```